Brand new letterhead, business card, email signature etc.

We are a financial company in London, UK. Our website is www.quorvane.com. We're wanting a complete remodel of the company colours, letter head, business cards, email signatures, etc. Looking to keep the same font for the company name. I have upload a colour palette that we want to work with. We're looking for company letterhead for outgoing letters/ correspondence, letterhead for internal documentation, email signatures, e-letters. etc. Ultimately we will redesign the entire website also. It is important that our clients get a strong, secure, warm, trustworthy, solid feeling and first impression.
Updates

Designs look the same

Target Market(s)

Institutional investors, (ultra) high net worth individuals

Industry/Entity Type

Finance, Invesments banking.

Font styles to use
Other font styles liked:
• Current font is "Champagne & Limousines"

Requirements
Must have
• Must use the colours provided on the PDF uploaded to the portal. The purple = main colour. The red = accent colour.
Nice to have
• Nice to use same font as now for the company name "Marlowin". Font is "Champagne & Limousines". Nice to have some reference to the old logo flower, but only subtle.
Should not have
• Do not use the colour red from our website. Use the colours provided on the colour palette PDF that I uploaded in the portal.

```html
<!DOCTYPE html>
<html lang="en">
<head>
<meta charset="utf-8">
<title>Marlowin Stationery</title>
<link href="https://fonts.googleapis.com/css2?family=Josefin+Sans:wght@300;400;600&display=swap" rel="stylesheet">
<style>
:root{
  --purple:#22001a;
  --red:#c42a1d;
  --paper:#f2f2f1;
  --ink:#2a2a2a;
  --muted:#6d6d6d;
  --bg:#e3e3e5;
}
*{box-sizing:border-box;margin:0;padding:0}
html,body{width:1200px;height:792px;overflow:hidden;background:var(--bg);font-family:"Josefin Sans",sans-serif;color:var(--ink)}
.canvas{position:relative;width:1200px;height:792px}
.piece{position:absolute;background:var(--paper);overflow:hidden}
.brand{position:absolute;display:flex;align-items:center;white-space:nowrap}
.brand-square{border:1px solid var(--ink);flex:none}
.brand-name{font-weight:300;letter-spacing:.22em;color:var(--ink);line-height:1}

/* business card front */
.card-front{left:184px;top:132px;width:170px;height:97px;background:var(--purple)}
.card-front .band{position:absolute;left:0;right:0;top:29px;height:39px;background:var(--paper)}
.card-front .brand{left:24px;top:36px;gap:7px}
.card-front .brand-square{width:24px;height:24px}
.card-front .brand-name{font-size:14px}

/* business card back */
.card-back{left:379px;top:132px;width:170px;height:97px}
.frame{position:absolute;border:1.5px solid var(--purple)}
.card-back .frame{left:7px;top:7px;width:156px;height:83px}
.card-back .brand{left:43px;top:26px;gap:5px}
.card-back .brand-square{width:16px;height:16px}
.card-back .brand-name{font-size:9.5px}

.contact-strip{position:absolute;color:var(--red);text-align:center;border-top:.6px solid var(--ink);border-bottom:.6px solid var(--ink)}
.contact-strip .addr{border-bottom:.6px solid var(--ink)}
.contact-strip .links{display:flex}
.contact-strip .links span{flex:1}
.contact-strip .links span+span{border-left:.6px solid var(--ink)}
.card-back .contact-strip{left:35px;top:63px;width:99px;font-size:3.6px;line-height:8px}

/* compliment slip */
.slip{left:184px;top:255px;width:365px;height:182px}
.slip .frame{left:14px;top:13px;width:334px;height:153px}
.slip .brand{left:117px;top:42px;gap:9px}
.slip .brand-square{width:30px;height:28px}
.slip .brand-name{font-size:16px}
.slip .contact-strip{left:117px;top:130px;width:130px;font-size:5px;line-height:11px}

/* envelope */
.envelope{left:184px;top:469px;width:365px;height:182px}
.envelope .flap{position:absolute;left:0;top:0;width:365px;height:46px}
.envelope .brand{left:104px;top:80px;gap:14px}
.envelope .brand-square{width:33px;height:33px}
.envelope .brand-name{font-size:19px}

/* letterhead */
.letter{left:595px;top:131px;width:367px;height:519px;background:var(--purple)}
.letter .sheet{position:absolute;left:18px;right:18px;top:0;bottom:0;background:var(--paper)}
.letter .tab-top{position:absolute;left:0;top:0;width:201px;height:19px;background:var(--purple);border-bottom-right-radius:18px}
.letter .tab-bottom{position:absolute;right:0;bottom:0;left:173px;height:19px;background:var(--purple);border-top-left-radius:18px}
.letter .rule-top{position:absolute;left:201px;right:18px;top:9px;height:1px;background:var(--red)}
.letter .rule-bottom{position:absolute;left:18px;width:155px;bottom:9px;height:1px;background:var(--red)}
.letter .brand{left:40px;top:42px;gap:9px}
.letter .brand-square{width:37px;height:33px}
.letter .brand-name{font-size:21px}

.sender{position:absolute;left:39px;top:133px;padding-left:5px;border-left:.7px solid var(--ink);font-size:4.6px;line-height:7.2px;color:var(--ink)}
.sender .name{font-size:7.4px;font-weight:600;letter-spacing:.02em;line-height:8px}
.sender .role{font-size:4.8px;letter-spacing:.25em;color:var(--muted);margin-bottom:4px}
.label{color:var(--red)}
.date{position:absolute;right:41px;top:176px;font-size:5.3px}

.body{position:absolute;left:39px;top:208px;width:288px;font-size:6.7px;line-height:8.1px;font-weight:300;text-align:justify;color:#3a3a3a}
.body p+p{margin-top:8.2px}

.sign{position:absolute;right:41px;top:352px;text-align:right}
.sign .signature{display:block;width:66px;height:21px;margin-left:auto;background:linear-gradient(90deg,rgba(34,0,26,.05),rgba(34,0,26,.14),rgba(34,0,26,.05));border-radius:2px}
.sign .name{font-size:7.4px;font-weight:600;letter-spacing:.03em;margin-top:3px}
.sign .role{font-size:5px;letter-spacing:.3em;color:var(--muted)}

.footer{position:absolute;left:0;right:0;top:443px;font-size:5px;line-height:6.5px}
.footer .item{position:absolute;display:flex;align-items:center;gap:7px}
.footer svg{width:10px;height:10px;flex:none}
</style>
</head>
<body>
<div class="canvas">

  <div class="piece card-front">
    <div class="band"></div>
    <div class="brand"><span class="brand-square"></span><span class="brand-name">MARLOWIN</span></div>
  </div>

  <div class="piece card-back">
    <div class="frame"></div>
    <div class="brand"><span class="brand-square"></span><span class="brand-name">MARLOWIN</span></div>
    <div class="contact-strip">
      <div class="addr">24 Fenwick Row, London EC2V 7HN, UK.</div>
      <div class="links"><span>www.quorvane.com</span><span>info@quorvane.com</span></div>
    </div>
  </div>

  <div class="piece slip">
    <div class="frame"></div>
    <div class="brand"><span class="brand-square"></span><span class="brand-name">MARLOWIN</span></div>
    <div class="contact-strip">
      <div class="addr">24 Fenwick Row, London EC2V 7HN, UK.</div>
      <div class="links"><span>www.quorvane.com</span><span>info@quorvane.com</span></div>
    </div>
  </div>

  <div class="piece envelope">
    <svg class="flap" viewBox="0 0 365 46" preserveAspectRatio="none">
      <path d="M0 0 H365 L362 30 Q360 45 344 45 H22 Q6 45 4 30 Z" fill="var(--purple)"/>
    </svg>
    <div class="brand"><span class="brand-square"></span><span class="brand-name">MARLOWIN</span></div>
  </div>

  <div class="piece letter">
    <div class="sheet"></div>
    <div class="tab-top"></div>
    <div class="tab-bottom"></div>
    <div class="rule-top"></div>
    <div class="rule-bottom"></div>

    <div class="brand"><span class="brand-square"></span><span class="brand-name">MARLOWIN</span></div>

    <div class="sender">
      <div class="name">ELSBETH R. CARROW</div>
      <div class="role">MARKETING MANAGER</div>
      <div><span class="label">PHONE :</span> +44-20-7946-0381</div>
      <div><span class="label">WEB :</span> www.quorvane.com</div>
      <div><span class="label">ADDR :</span> 18 HARROWGATE LANE</div>
      <div>ISLINGTON, LONDON N1 4QT</div>
    </div>

    <div class="date"><span class="label">DATE :</span> 26-July-2015</div>

    <div class="body">
      <p>Lorem ipsum dolor sit amet, consectetur adipiscing elit, sed do eiusmod tempor incididunt ut labore et dolore magna aliqua. Quis ipsum suspendisse ultrices gravida. Risus commodo viverra maecenas accumsan lacus vel facilisis. Lorem ipsum dolor sit amet, consectetur adipiscing elit, sed do eiusmod tempor incididunt ut labore et dolore magna aliqua. Quis ipsum suspendisse ultrices gravida.</p>
      <p>Lorem ipsum dolor sit amet, consectetur adipiscing elit, sed do eiusmod tempor incididunt ut labore et dolore magna aliqua. Quis ipsum suspendisse ultrices gravida. Risus commodo viverra maecenas accumsan lacus vel facilisis. Lorem ipsum dolor sit amet consectetur adipiscing elit, sed do eiusmod tempor incididunt ut labore et dolore magna aliqua. Quis ipsum suspendisse ultrices gravida. Risus commodo viverra maecenas accumsan lacus vel facilisis.</p>
      <p>Lorem ipsum dolor sit amet, consectetur adipiscing elit, sed do eiusmod tempor incididunt ut labore et dolore magna aliqua. Quis ipsum suspendisse ultrices gravida. Risus commodo viverra maecenas accumsan lacus vel facilisis. Lorem ipsum dolor sit amet, consectetur adipiscing elit, sed do eiusmod tempor incididunt ut labore et dolore magna aliqua. Quis ipsum suspendisse ultrices gravida. Risus commodo viverra maecenas accumsan lacus vel facilisis.</p>
    </div>

    <div class="sign">
      <span class="signature" role="img" aria-label="Handwritten signature of the sender"></span>
      <div class="name">TOBIAS M. RENFIELD</div>
      <div class="role">CREATIVE DESIGNER</div>
    </div>

    <div class="footer">
      <div class="item" style="left:55px">
        <svg viewBox="0 0 24 24" aria-hidden="true"><path fill="var(--red)" d="M6.6 10.8a15.1 15.1 0 0 0 6.6 6.6l2.2-2.2c.3-.3.7-.4 1-.2 1.1.4 2.3.6 3.6.6.6 0 1 .4 1 1V20c0 .6-.4 1-1 1A17 17 0 0 1 3 4c0-.6.4-1 1-1h3.5c.6 0 1 .4 1 1 0 1.3.2 2.5.6 3.6.1.3 0 .7-.2 1z"/></svg>
        <div>+44-20-7946-0512<br>+44-20-7946-0512</div>
      </div>
      <div class="item" style="left:138px">
        <svg viewBox="0 0 24 24" aria-hidden="true"><circle cx="12" cy="12" r="9" fill="none" stroke="var(--red)" stroke-width="2.2"/><path d="M3 12h18M12 3c3 3 3 15 0 18M12 3c-3 3-3 15 0 18" fill="none" stroke="var(--red)" stroke-width="1.6"/></svg>
        <div>www.quorvane.com<br>office@quorvane.com</div>
      </div>
      <div class="item" style="left:242px">
        <svg viewBox="0 0 24 24" aria-hidden="true"><path fill="var(--red)" d="M12 2a7 7 0 0 0-7 7c0 5.3 7 13 7 13s7-7.7 7-13a7 7 0 0 0-7-7zm0 9.5A2.5 2.5 0 1 1 12 6.5a2.5 2.5 0 0 1 0 5z"/></svg>
        <div>52 Ashcombe Street<br>London, EC2M 3PL</div>
      </div>
    </div>
  </div>

</div>
</body>
</html>
```